Pain cream backed by Pro-Athletes "Glacier Ember"

Looking to revamp the label brand.
It's an all-natural pain gel. It heats then cools. Looking for a very sharp look that gets the point of the product use across.
Eveyrthing about the original label can be changed except for the text. It still needs to have the same information but can be any color, font whatever.,
I'll need pdf's and ai files of the design.
Label Size die line is attached.
Original Label is attached.

```html
<!DOCTYPE html>
<html lang="en">
<head>
<meta charset="utf-8">
<title>Glacier Ember — Label</title>
<link href="https://fonts.googleapis.com/css2?family=Arimo:wght@400&family=Roboto+Condensed:wght@300;700&display=swap" rel="stylesheet">
<style>
  :root {
    --page-bg: #f4f4f4;
    --cool-blue: #2f5fae;
    --pale-blue: #b9c6e4;
    --warm-orange: #e2601c;
    --hot-red: #e62a10;
    --label-text: #ffffff;
  }
  html, body {
    margin: 0;
    padding: 0;
    width: 1047px;
    height: 1200px;
    overflow: hidden;
    background: var(--page-bg);
  }
  .canvas {
    position: relative;
    width: 1047px;
    height: 1200px;
  }
  .label {
    position: absolute;
    left: 253px;
    top: 75px;
    width: 540px;
    height: 1050px;
    overflow: hidden;
  }
  .label-art {
    position: absolute;
    inset: 0;
    background: linear-gradient(180deg,
      var(--cool-blue) 0%,
      var(--pale-blue) 38%,
      var(--warm-orange) 60%,
      var(--hot-red) 100%);
  }
  .brand-name {
    position: absolute;
    left: 50px;
    top: 990px;
    transform: rotate(-90deg);
    transform-origin: 0 0;
    margin: 0;
    font-family: "Arimo", sans-serif;
    font-weight: 400;
    font-size: 86px;
    line-height: 86px;
    letter-spacing: 4px;
    white-space: nowrap;
    color: var(--label-text);
    text-transform: uppercase;
    display: flex;
    align-items: center;
    gap: 22px;
  }
  .brand-mark {
    width: 44px;
    height: 44px;
    background: var(--label-text);
    flex: none;
  }
  .tagline {
    position: absolute;
    right: 20px;
    top: 700px;
    margin: 0;
    font-family: "Roboto Condensed", sans-serif;
    font-weight: 700;
    font-size: 90px;
    line-height: 94px;
    letter-spacing: -1px;
    text-align: right;
    color: var(--label-text);
  }
  .net-volume {
    position: absolute;
    right: 22px;
    top: 958px;
    margin: 0;
    font-family: "Roboto Condensed", sans-serif;
    font-weight: 300;
    font-size: 32px;
    color: var(--label-text);
  }
</style>
</head>
<body>
<main class="canvas">
  <section class="label">
    <div class="label-art" role="img" aria-label="Background artwork: a cool-to-hot colour field moving from blue at the top to orange and red at the bottom"></div>

    <h1 class="brand-name"><span>Glacier Ember</span><span class="brand-mark"></span></h1>

    <p class="tagline">Gets You<br>Back Up</p>
    <p class="net-volume">100ml (3.2oz)</p>
  </section>
</main>
</body>
</html>
```